Halvorsen Plumbing LLC business card

Would like a modern looking business card with my new logo

Contact Information for Business Card

Dwight Halvorsen 2417 Birchmont Hollow Rd Elmhollow, VT 06512, Halvorsenplumbingllc@mailnest.example, 203-555-0184

```html
<!DOCTYPE html>
<html lang="en">
<head>
<meta charset="utf-8">
<title>Halvorsen Plumbing LLC – Business Card</title>
<link href="https://fonts.googleapis.com/css2?family=Saira:wght@400;700&display=swap" rel="stylesheet">
<style>
  :root {
    --backdrop: #acacac;
    --card-front: #ffffff;
    --card-back: #000000;
    --brand-blue: #00aeef;
    --ink: #111111;
    --muted: #9a9a9a;
    --back-mark: #2f2f2f;
  }
  html, body {
    margin: 0;
    padding: 0;
    width: 1200px;
    height: 1000px;
    overflow: hidden;
    background: var(--backdrop);
    font-family: "Saira", sans-serif;
  }
  .stage {
    position: relative;
    width: 1200px;
    height: 1000px;
  }
  .card {
    position: absolute;
    left: 294px;
    width: 613px;
    height: 352px;
    border-radius: 26px;
    overflow: hidden;
    box-shadow: 0 18px 40px rgba(0,0,0,0.35);
  }
  .card--front { top: 80px; background: var(--card-front); }
  .card--back { top: 496px; background: var(--card-back); }

  .brand-name {
    position: absolute;
    left: 71px;
    top: 70px;
    margin: 0;
    font-weight: 700;
    font-size: 20px;
    line-height: 1.1;
    letter-spacing: 1px;
    color: var(--ink);
    text-transform: uppercase;
  }
  .holder-name {
    position: absolute;
    left: 71px;
    top: 143px;
    margin: 0;
    font-weight: 700;
    font-size: 19px;
    letter-spacing: 0.5px;
    color: var(--brand-blue);
    text-transform: uppercase;
  }
  .contact {
    position: absolute;
    left: 71px;
    margin: 0;
    font-weight: 400;
    font-size: 19px;
    line-height: 23px;
    color: var(--muted);
    font-style: normal;
  }
  .contact--address { top: 192px; }
  .contact--reach { top: 259px; }
  .corner-accent {
    position: absolute;
    right: 0;
    bottom: 0;
  }
  .back-name {
    position: absolute;
    left: 0;
    right: 0;
    top: 150px;
    margin: 0;
    text-align: center;
    font-weight: 700;
    font-size: 34px;
    letter-spacing: 2px;
    color: var(--back-mark);
    text-transform: uppercase;
  }
</style>
</head>
<body>
<main class="stage">
  <section class="card card--front">
    <p class="brand-name">Halvorsen Plumbing LLC</p>
    <h1 class="holder-name">Dwight Halvorsen</h1>
    <address class="contact contact--address">2417 Birchmont Hollow Rd<br>Elmhollow, VT 06512</address>
    <p class="contact contact--reach">203-555-0184<br>Halvorsenplumbingllc@mailnest.example</p>
    <svg class="corner-accent" width="275" height="74" viewBox="0 0 275 74" aria-hidden="true">
      <polygon points="0,74 275,0 275,74" fill="var(--brand-blue)"/>
    </svg>
  </section>
  <section class="card card--back">
    <p class="back-name">Halvorsen Plumbing LLC</p>
  </section>
</main>
</body>
</html>
```